limo company looking for a graphic business card with professional look and feel

Looking for a business card design that can give you the full picture of the limo company by looking at the card - we provide airport service, wedding, birthday, night out, etc... we have sedans, suvs , limos, and party buses. I want the business card to have a professional look because we are targetting corporate clients as well as regular retail.
Info about the business can be found at: http://lnk.example.test/Qm4Tz
Target Market(s)
corporate clients and retail
Industry/Entity Type
Business
Contact Information for Business Card
I would like the logo and the name of the company to be in raised print - not sure if design makes a difference for that or just print - I need it designed in 350dpi
Requirements
Must have
- pictures of vehicle types (sedans, suvs, limos, party bus). pictures of interior of the limos if possible. list service types (weddings, birthdays, proms, airport transportation) & service areas (houston, the woodlands, spring, tomball, cypress, kingwood).
Nice to have
- nice professional look to it.

```html
<!DOCTYPE html>
<html lang="en">
<head>
<meta charset="utf-8">
<title>Crestline Limousine &amp; Transportation – Business Card</title>
<link rel="stylesheet" href="https://fonts.googleapis.com/css2?family=Arimo:wght@400;700&display=swap">
<style>
  :root {
    --page: #e9e9e9;
    --card-brown: #4a3425;
    --card-brown-light: #5c4130;
    --card-brown-dark: #3a271b;
    --band: #343336;
    --gold: #c9a25e;
    --white: #ffffff;
    --photo-warm: #7a4a2c;
    --photo-cool: #2f3e5c;
  }
  * { box-sizing: border-box; margin: 0; padding: 0; }
  html, body { width: 1028px; height: 1200px; overflow: hidden; }
  body {
    background: var(--page);
    font-family: "Arimo", Arial, sans-serif;
    position: relative;
  }
  .card {
    position: absolute;
    left: 22px;
    width: 964px;
    height: 556px;
    background: var(--card-brown);
    box-shadow: 4px 6px 12px rgba(0,0,0,0.35);
    overflow: hidden;
  }
  .card--front { top: 12px; }
  .card--back { top: 603px; width: 966px; }

  .fleet-collage {
    position: absolute;
    left: 206px; top: 91px;
    width: 552px; height: 208px;
    background: linear-gradient(90deg, var(--photo-cool) 0%, var(--photo-warm) 35%, #b78a62 60%, #d8d2cc 85%, var(--photo-cool) 100%);
    box-shadow: 0 2px 6px rgba(0,0,0,0.4);
  }

  .brand {
    position: absolute;
    left: 0; right: 0;
    text-align: center;
    color: var(--gold);
  }
  .brand__name { font-weight: 700; font-size: 34px; letter-spacing: 0.5px; line-height: 1; }
  .brand__tag { font-weight: 700; font-size: 22px; line-height: 1; margin-top: 8px; }
  .card--front .brand { top: 368px; }

  .web-band {
    position: absolute;
    left: 0; right: 0; top: 470px;
    height: 33px;
    background: var(--band);
    color: var(--white);
    font-size: 21px;
    text-align: center;
    line-height: 33px;
  }

  .pattern {
    position: absolute; inset: 0;
    background:
      radial-gradient(circle at 30% 40%, var(--card-brown-light) 0%, transparent 55%),
      radial-gradient(circle at 80% 70%, var(--card-brown-light) 0%, transparent 50%),
      var(--card-brown-dark);
  }

  .contact-list { position: absolute; left: 52px; top: 86px; list-style: none; }
  .contact {
    position: relative;
    padding-left: 44px;
    color: var(--white);
    font-size: 23px;
    line-height: 30px;
  }
  .contact svg { position: absolute; left: 0; top: 4px; width: 20px; height: 20px; }
  .icon-solid { fill: var(--white); }
  .icon-line { fill: none; stroke: var(--white); stroke-width: 1.3; }
  .icon-cut { fill: var(--card-brown); }
  .contact--toll { margin-bottom: 37px; }
  .contact--local { margin-bottom: 41px; }
  .contact--email { margin-bottom: 30px; }
  .contact--address { margin-bottom: 20px; line-height: 29.5px; }

  .card--back .brand { left: auto; right: 52px; top: 430px; width: 300px; }
  .card--back .brand__name { font-size: 27px; }
  .card--back .brand__tag { font-size: 18px; margin-top: 6px; }
</style>
</head>
<body>
  <section class="card card--front">
    <div class="fleet-collage" role="img" aria-label="Collage of sedans, SUV and stretch limousines with limo interiors, corporate passengers and a wedding couple"></div>
    <div class="brand">
      <div class="brand__name">Crestline Limousine</div>
      <div class="brand__tag">&amp; Transportation</div>
    </div>
    <div class="web-band">www.crestlinelimo.example</div>
  </section>

  <section class="card card--back">
    <div class="pattern" role="img" aria-label="Faint floral pattern in warm brown tones"></div>
    <ul class="contact-list">
      <li class="contact contact--toll">
        <svg viewBox="0 0 20 20"><rect class="icon-solid" x="5.5" y="1" width="9" height="18" rx="2"/><rect class="icon-cut" x="7" y="3.5" width="6" height="11"/></svg>
        Toll Free: 800-555-0182
      </li>
      <li class="contact contact--local">
        <svg viewBox="0 0 20 20"><rect class="icon-solid" x="5.5" y="1" width="9" height="18" rx="2"/><rect class="icon-cut" x="7" y="3.5" width="6" height="11"/></svg>
        Local: 832-555-0147
      </li>
      <li class="contact contact--email">
        <svg viewBox="0 0 20 20"><rect class="icon-solid" x="1" y="4" width="18" height="12"/><path d="M1 4 L10 11.5 L19 4" stroke="#4a3425" stroke-width="1.4" fill="none"/></svg>
        service@crestlinelimo.example
      </li>
      <li class="contact contact--address">
        <svg viewBox="0 0 20 20"><path class="icon-solid" d="M10 1 C6.3 1 4.2 3.7 4.2 6.8 C4.2 10.5 10 19 10 19 C10 19 15.8 10.5 15.8 6.8 C15.8 3.7 13.7 1 10 1 Z"/><circle class="icon-cut" cx="10" cy="6.8" r="2.1"/></svg>
        Fleet Office<br>1870 Meridian Parkway,<br>Oak Hollow, TX 77999
      </li>
      <li class="contact contact--web">
        <svg viewBox="0 0 20 20"><g class="icon-line"><circle cx="10" cy="10" r="8.5"/><ellipse cx="10" cy="10" rx="4" ry="8.5"/><path d="M10 1.5 V18.5 M1.5 10 H18.5 M3 5.5 H17 M3 14.5 H17"/></g></svg>
        www.crestlinelimo.example
      </li>
    </ul>
    <div class="brand">
      <div class="brand__name">Crestline Limousine</div>
      <div class="brand__tag">&amp; Transportation</div>
    </div>
  </section>
</body>
</html>
```